Corvane Lending Partners. Professional and Established Company

A full service finance company specializing in obtaining capital for small business. Business Lending advisor, helping small business owners access the capital they need to launch, grow, or sustain their business. Many of our programs offer flexible guidelines to overcome common obstacles such as credit score, credit history, and time in business, financials, and industry type. Our streamlined funding process makes getting a business loan, business line of credit, stated income commercial real estate loan, a smooth and stress free experience.SOME OF THE MOST COMMON NEEDS FOR BUSINESS CAPITAL:• Working Capital• Debt Consolidations (loans, merchant cash advances, etc.)• Payroll• Operating Expenses• Inventory• Equipment Financing• Commercial Real Estate (Purchase, Fix & Flip, Rehab, Renovations)• Business Acquisitions• Business ExpansionWe like the websites:www.brookfellcap.com they are in the same industry and provide the same servicesWe are wanting to be able to update when we do press releases and such using Word Press. Our look should be very professional and we will be adding Our Team Professional Bios and Headshots.

Industry/Entity Type

Finance

Number of Pages Required

5+ page

Font styles to use
Serif
Sans Serif

Requirements
Must have
• We want to copy brookfellcap.com
• We need:
• Home Page
• About Us
• Loan Programs
• Loan Criteria
• News
• Apply Now
• Contact
Nice to have
• See brookfellcap.com
Should not have
• Need professional design. Nothing bright or abstract

```html
<!DOCTYPE html>
<html lang="en">
<head>
<meta charset="utf-8">
<title>Corvane Lending Partners</title>
<link rel="stylesheet" href="https://fonts.googleapis.com/css2?family=Merriweather:wght@400;700&family=Montserrat:wght@400;500;600;700&family=Roboto:ital,wght@1,300;1,400&display=swap">
<style>
:root{
  --black:#050505;
  --white:#ffffff;
  --brand-blue:#2b6fb3;
  --nav-grey:#555c66;
  --green:#2db52d;
  --money-green:#27e22a;
  --sky-top:#2c4f8f;
  --sky-mid:#3f6fb8;
  --glass:#5d8fd6;
  --band:rgba(40,50,70,.55);
  --vault-dark:#1b1b1c;
  --vault-mid:#3b3b3d;
}
*{box-sizing:border-box;margin:0;padding:0}
html,body{width:1093px;height:1200px;overflow:hidden;background:var(--white)}
body{position:relative;font-family:"Montserrat",sans-serif;color:var(--white)}
.topbar{position:absolute;top:0;left:0;width:1093px;height:40px;background:var(--black);font-size:11.5px;font-weight:500}
.topbar span{position:absolute;top:13px;display:flex;align-items:center;gap:5px}
.lang{left:102px;font-weight:600}
.phone{left:539px}
.email{left:716px}
.social{left:957px;top:14px!important;width:12px;height:12px;background:var(--brand-blue);border-radius:2px}
.header{position:absolute;top:40px;left:0;width:1093px;height:81px;background:var(--white);border-bottom:1px solid #d8dde3}
.brand{position:absolute;left:102px;top:24px;font-family:"Merriweather",serif;font-weight:700;font-size:22px;color:var(--brand-blue);line-height:1.1;width:220px}
.nav{position:absolute;right:105px;top:31px;display:flex;gap:11px;font-size:12.8px;font-weight:600;color:var(--nav-grey)}
.hero{position:absolute;top:121px;left:0;width:1093px;height:711px}
.hero-photo{position:absolute;inset:0;background:
  linear-gradient(115deg,var(--sky-top) 0%,var(--sky-mid) 38%,var(--glass) 60%,#9ec2ee 78%,#3b63a8 100%)}
.headline{position:absolute;left:101px;top:118px;font-family:"Merriweather",serif;font-weight:400;font-size:82px;line-height:104px;color:var(--white)}
.apply-btn{position:absolute;left:644px;top:233px;width:106px;height:65px;background:var(--green);border:2px solid #e8f5e8;border-radius:3px;display:flex;align-items:center;justify-content:center;font-weight:700;font-size:14px}
.intro{position:absolute;left:104px;top:333px;font-size:19px;line-height:24.5px;font-weight:500}
.closed-title{position:absolute;top:480px;width:100%;text-align:center;font-size:24px;font-weight:500;letter-spacing:.5px}
.loan-band{position:absolute;top:530px;left:0;width:1093px;height:129px;background:var(--band)}
.loan{position:absolute;top:0;height:129px;border-left:1px solid var(--white);border-right:1px solid var(--white);text-align:center;font-family:"Roboto",sans-serif;font-style:italic;font-weight:300;font-size:19px;line-height:19.5px;padding-top:18px}
.loan .amount{display:block;font-family:"Montserrat",sans-serif;font-style:normal;font-weight:700;color:var(--money-green);font-size:19px;margin:12px 0 5px}
.video{position:absolute;top:832px;left:0;width:1093px;height:368px;overflow:hidden}
.video-photo{position:absolute;inset:0;background:radial-gradient(ellipse at 50% 30%,var(--vault-mid) 0%,#2a2a2c 45%,var(--vault-dark) 100%)}
.video-cta{position:absolute;top:212px;width:100%;text-align:center;font-size:24.5px;font-weight:500}
.play{position:absolute;left:487px;top:293px}
</style>
</head>
<body>
<div class="topbar">
  <span class="lang">ENGLISH
    <svg width="9" height="7" viewBox="0 0 9 7"><path d="M1 1.5l3.5 3.5L8 1.5" stroke="#fff" stroke-width="2" fill="none"/></svg></span>
  <span class="phone"><svg width="9" height="9" viewBox="0 0 10 10"><path d="M2 0l2 2.5-1 1.2a6 6 0 003.3 3.3l1.2-1L10 8 8.5 10C4 9.5.5 6 0 1.5z" fill="#36b6e0"/></svg>+1 (555) 014-2290</span>
  <span class="email"><svg width="11" height="8" viewBox="0 0 11 8"><rect width="11" height="8" rx="1" fill="#2db52d"/><path d="M0 .5l5.5 4 5.5-4" stroke="#050505" fill="none"/></svg>info@corvanelending.com</span>
  <span class="social"></span>
</div>
<header class="header">
  <div class="brand">Corvane Lending Partners</div>
  <nav class="nav"><span>ABOUT US</span><span>LOAN PROGRAMS</span><span>LOAN CRITERIA</span><span>NEWS</span><span>APPLY NOW</span><span>CONTACT</span></nav>
</header>
<section class="hero">
  <div class="hero-photo" role="img" aria-label="Glass office tower against a blue sky"></div>
  <h1 class="headline">Think<br>Monumental</h1>
  <div class="apply-btn">APPLY NOW</div>
  <p class="intro">Welcome To Corvane Lending Partners.<br>The nation’s most unique private lender to<br>commercial real estate market.</p>
  <h2 class="closed-title">RECENTLY CLOSED LOANS</h2>
  <div class="loan-band">
    <div class="loan" style="left:102px;width:204px">Office Building<span class="amount">$1,400,000</span>Townhouse<br>Manhattan,NY</div>
    <div class="loan" style="left:330px;width:204px">Mixed Use<span class="amount">$13,400,000</span>Land Development<br>Manhattan,NY</div>
    <div class="loan" style="left:558px;width:204px">Retail Development<span class="amount">$19,900,000</span>Land Acquisition<br>Mansfield,Texas</div>
    <div class="loan" style="left:786px;width:204px">Hotel<span class="amount">$31,400,000</span>Acquisition<br>New York,New York</div>
  </div>
</section>
<section class="video">
  <div class="video-photo" role="img" aria-label="Stone vaulted arcade in dim light"></div>
  <p class="video-cta">Click here to view a comprehensive video of our services</p>
  <svg class="play" width="118" height="118" viewBox="0 0 118 118"><circle cx="59" cy="59" r="59" fill="#fff"/><path d="M41 30v58l50-29z" fill="#1e1e1e"/></svg>
</section>
</body>
</html>
```